Business Card Design

After a corporate career in the finance sector I am now operating on my own as a consultant. I require a simple design, and want a strong card which is targeted at a conservative audience.

Target Market(s)

highly educated senior management, directors of companies, finance sector

Industry/Entity Type

Conservative

Contact Information for Business Card

Ruth Danver
Consultant
Mobile: 0417 862 450
Email: ruth.danv@mailcove.net

Requirements
Should not have
• I don't want the colours green/yellow/brown

```html
<!DOCTYPE html>
<html lang="en">
<head>
<meta charset="utf-8">
<title>Ruth Danver – Business Card</title>
<link rel="stylesheet" href="https://fonts.googleapis.com/css2?family=Noto+Sans:wght@400;700&display=swap">
<style>
  :root {
    --backdrop: #e6e7e9;
    --card-grey: #939598;
    --card-light: #ffffff;
    --accent-blue: #0077c2;
    --ink: #0d0d0d;
    --contact-ink: #ffffff;
  }
  html, body {
    margin: 0;
    padding: 0;
    width: 1200px;
    height: 1200px;
    overflow: hidden;
    background: var(--backdrop);
  }
  .canvas {
    position: relative;
    width: 1200px;
    height: 1200px;
  }
  .business-card {
    position: absolute;
    left: 134px;
    top: 319px;
    width: 928px;
    height: 560px;
    overflow: hidden;
    font-family: "Noto Sans", Verdana, sans-serif;
    background: radial-gradient(circle 330px at 346px 150px, var(--card-light) 0%, #eeeeef 35%, var(--card-grey) 100%);
    background-color: var(--card-grey);
  }
  .accent-band {
    position: absolute;
    left: 0;
    top: 222px;
    width: 928px;
    height: 10px;
    background: var(--accent-blue);
  }
  .identity {
    position: absolute;
    left: 215px;
    top: 60px;
    color: var(--ink);
  }
  .identity__name {
    margin: 0;
    font-size: 58px;
    font-weight: 700;
    line-height: 1;
    letter-spacing: 1px;
  }
  .identity__role {
    margin: 8px 0 0 2px;
    font-size: 45px;
    font-weight: 400;
    line-height: 1;
  }
  .contacts {
    position: absolute;
    left: 486px;
    top: 414px;
    margin: 0;
    padding: 0;
    list-style: none;
    color: var(--contact-ink);
    font-size: 33px;
    letter-spacing: 0.5px;
  }
  .contacts__item {
    display: flex;
    align-items: center;
    height: 44px;
  }
  .contacts__icon {
    width: 30px;
    height: 30px;
    margin-right: 12px;
    flex: none;
  }
</style>
</head>
<body>
<main class="canvas">
  <section class="business-card" aria-label="Business card for Ruth Danver">
    <div class="accent-band" aria-hidden="true"></div>

    <header class="identity">
      <h1 class="identity__name">Ruth Danver</h1>
      <p class="identity__role">Consultant</p>
    </header>

    <ul class="contacts">
      <li class="contacts__item">
        <svg class="contacts__icon" viewBox="0 0 30 30" aria-hidden="true">
          <circle cx="15" cy="15" r="14" fill="#ffffff"/>
          <rect x="10" y="5" width="10" height="20" rx="1.5" fill="var(--accent-blue)"/>
          <rect x="11.8" y="7.5" width="6.4" height="6" fill="#ffffff"/>
          <g fill="#ffffff">
            <rect x="12" y="16" width="1.6" height="1.4"/><rect x="14.2" y="16" width="1.6" height="1.4"/><rect x="16.4" y="16" width="1.6" height="1.4"/>
            <rect x="12" y="18.6" width="1.6" height="1.4"/><rect x="14.2" y="18.6" width="1.6" height="1.4"/><rect x="16.4" y="18.6" width="1.6" height="1.4"/>
            <rect x="12" y="21.2" width="1.6" height="1.4"/><rect x="14.2" y="21.2" width="1.6" height="1.4"/><rect x="16.4" y="21.2" width="1.6" height="1.4"/>
          </g>
        </svg>
        <span class="contacts__text">0417 862 450</span>
      </li>
      <li class="contacts__item">
        <svg class="contacts__icon" viewBox="0 0 30 30" aria-hidden="true">
          <circle cx="15" cy="15" r="14" fill="#ffffff"/>
          <rect x="5" y="9" width="20" height="13" fill="var(--accent-blue)"/>
          <path d="M5.5,9.5 L15,16.5 L24.5,9.5 M5.5,21.5 L12,15 M24.5,21.5 L18,15" fill="none" stroke="#ffffff" stroke-width="1.3"/>
        </svg>
        <span class="contacts__text">ruth.danv@mailcove.net</span>
      </li>
    </ul>
  </section>
</main>
</body>
</html>
```